Business Card Design Project

i need a bussines car design
Velora Clinical Hypnotherapy

Daniel Herwood
Psychotherapy & Hypnosis

94265831 /0417529046

back of the card appoinment space.

file was provided on a PDF, LOgo , use the blu colorsa as well , elegant, clear,

Target Market(s)

young professional, caucasian , young mothers.

Industry/Entity Type

Business

```html
<!DOCTYPE html>
<html lang="en">
<head>
<meta charset="utf-8">
<title>Velora Clinical Hypnotherapy – Business Card</title>
<link href="https://fonts.googleapis.com/css2?family=Open+Sans:wght@400;600;700&display=swap" rel="stylesheet">
<style>
  :root {
    --brand-blue: #1a74c4;
    --brand-blue-deep: #1565b0;
    --text-blue: #1e6fbf;
    --paper: #ffffff;
    --line: #9a9a9a;
    --stage: #eceff2;
    --photo-light: #e9dccb;
    --photo-mid: #c99b7c;
  }
  * { margin: 0; padding: 0; box-sizing: border-box; }
  html, body { width: 1200px; height: 789px; overflow: hidden; }
  body {
    position: relative;
    background: var(--stage);
    font-family: "Open Sans", Arial, sans-serif;
    color: var(--text-blue);
  }
  .card {
    position: absolute;
    background: var(--paper);
    overflow: hidden;
    box-shadow: 0 3px 10px rgba(0,0,0,.25);
  }

  /* Front */
  .card-front { left: 137px; top: 49px; width: 568px; height: 318px; }
  .front-brand-panel { position: absolute; left: 0; top: 0; width: 286px; height: 286px; }
  .brand-name {
    position: absolute; left: 0; width: 286px; top: 128px;
    text-align: center; font-size: 24px; font-weight: 400; color: var(--text-blue);
    letter-spacing: .3px;
  }
  .brand-rule {
    position: absolute; left: 34px; width: 220px; top: 166px;
    border-top: 1px solid var(--text-blue);
  }
  .brand-web {
    position: absolute; left: 0; width: 286px; top: 170px;
    text-align: center; font-size: 10px; color: #555; letter-spacing: .4px;
  }
  .practitioner-name {
    position: absolute; left: 0; width: 286px; top: 226px;
    text-align: center; font-size: 15px;
  }
  .practitioner-role {
    position: absolute; left: 0; width: 286px; top: 245px;
    text-align: center; font-size: 12px;
  }
  .front-photo-panel {
    position: absolute; left: 286px; top: 0; width: 282px; height: 286px;
    background: var(--brand-blue);
  }
  .portrait {
    position: absolute; left: 22px; bottom: 0; width: 250px; height: 244px;
    background: radial-gradient(ellipse at 45% 35%, var(--photo-mid) 0 22%, var(--photo-light) 45%, #f3ebe0 100%);
    border-radius: 90px 90px 0 0;
  }
  .front-band-left {
    position: absolute; left: 0; top: 286px; width: 286px; height: 32px;
    background: var(--brand-blue);
  }
  .front-phone {
    position: absolute; left: 286px; top: 286px; width: 282px; height: 32px;
    display: flex; align-items: center; justify-content: center; gap: 6px;
    font-size: 13px;
  }
  .front-phone svg { width: 13px; height: 13px; }

  /* Back */
  .card-back { left: 479px; top: 416px; width: 569px; height: 319px; }
  .appointments-panel { position: absolute; left: 0; top: 0; width: 289px; height: 287px; }
  .appointments-title {
    position: absolute; left: 0; width: 289px; top: 40px;
    text-align: center; font-size: 14px; font-weight: 700;
  }
  .appointment-row {
    position: absolute; left: 13px; display: flex; align-items: flex-end;
    font-size: 13px; color: #8a8a8a;
  }
  .appointment-row .blank { display: inline-block; border-bottom: 1px solid var(--line); height: 14px; }
  .appointment-row .slash { margin: 0 1px; }
  .registration {
    position: absolute; left: 0; width: 289px; top: 262px;
    text-align: center; font-size: 16px;
  }
  .contact-panel {
    position: absolute; left: 289px; top: 0; width: 280px; height: 287px;
    background: var(--brand-blue); color: var(--paper); text-align: center;
  }
  .contact-heading { margin-top: 40px; font-size: 14px; font-weight: 700; }
  .contact-line { font-size: 13.5px; line-height: 19px; }
  .contact-email { font-size: 10.5px; font-weight: 600; line-height: 16px; }
  .contact-rule { width: 210px; margin: 26px auto 0; border-top: 1px solid rgba(255,255,255,.8); }
  .reschedule-note { margin-top: 30px; font-size: 12.5px; line-height: 17px; }
  .back-band-left {
    position: absolute; left: 0; top: 287px; width: 289px; height: 32px;
    background: var(--brand-blue);
  }
  .membership {
    position: absolute; left: 289px; top: 287px; width: 280px; height: 32px;
    display: flex; align-items: center; justify-content: center; gap: 6px;
    font-size: 16px;
  }
  .membership-badge {
    width: 36px; height: 36px; border-radius: 50%;
    background: #e8efe2; border: 2px solid #7cae4a;
  }
</style>
</head>
<body>

<section class="card card-front">
  <div class="front-brand-panel">
    <div class="brand-name">Velora Hypnotherapy</div>
    <div class="brand-rule"></div>
    <div class="brand-web">www.veloraclinicalhypnotherapy.com.au</div>
    <div class="practitioner-name">Daniel Herwood</div>
    <div class="practitioner-role">Psychotherapy &amp; Hypnosis</div>
  </div>
  <div class="front-photo-panel">
    <div class="portrait" role="img" aria-label="Portrait photo of the practitioner smiling, wearing glasses and a light shirt"></div>
  </div>
  <div class="front-band-left"></div>
  <div class="front-phone">
    <svg viewBox="0 0 24 24" aria-hidden="true"><path fill="none" stroke="#1e6fbf" stroke-width="2" d="M7 3l3 4-2 2c1 3 4 6 7 7l2-2 4 3-2 3C10 20 4 14 3 6z"/></svg>
    <span>94265831 / 0417529046</span>
  </div>
</section>

<section class="card card-back">
  <div class="appointments-panel">
    <div class="appointments-title">Your Appointments</div>

    <div class="appointment-row" style="top:72px">1.<span class="blank" style="width:30px"></span>am/pm&nbsp;<span class="blank" style="width:90px"></span>&nbsp;<span class="blank" style="width:26px"></span><span class="slash">/</span><span class="blank" style="width:20px"></span><span class="slash">/</span><span class="blank" style="width:22px"></span></div>
    <div class="appointment-row" style="top:108px">2.<span class="blank" style="width:30px"></span>am/pm&nbsp;<span class="blank" style="width:90px"></span>&nbsp;<span class="blank" style="width:26px"></span><span class="slash">/</span><span class="blank" style="width:20px"></span><span class="slash">/</span><span class="blank" style="width:22px"></span></div>
    <div class="appointment-row" style="top:144px">3.<span class="blank" style="width:30px"></span>am/pm&nbsp;<span class="blank" style="width:90px"></span>&nbsp;<span class="blank" style="width:26px"></span><span class="slash">/</span><span class="blank" style="width:20px"></span><span class="slash">/</span><span class="blank" style="width:22px"></span></div>
    <div class="appointment-row" style="top:180px">4.<span class="blank" style="width:30px"></span>am/pm&nbsp;<span class="blank" style="width:90px"></span>&nbsp;<span class="blank" style="width:26px"></span><span class="slash">/</span><span class="blank" style="width:20px"></span><span class="slash">/</span><span class="blank" style="width:22px"></span></div>
    <div class="appointment-row" style="top:216px">5.<span class="blank" style="width:30px"></span>am/pm&nbsp;<span class="blank" style="width:90px"></span>&nbsp;<span class="blank" style="width:26px"></span><span class="slash">/</span><span class="blank" style="width:20px"></span><span class="slash">/</span><span class="blank" style="width:22px"></span></div>

    <div class="registration">NHRA Registration No. NPM058214</div>
  </div>

  <div class="contact-panel">
    <div class="contact-heading">VELORA Clinical Hypnotherapy</div>
    <div class="contact-line">By Appointment . Phone: 0417 529 046</div>
    <div class="contact-line">148 Marlow rd Kensington</div>
    <div class="contact-email">info@veloraclinicalhypnotherapy.com.au</div>
    <div class="contact-rule"></div>
    <p class="reschedule-note">To reschedule your appointment,<br>please SMS or phone<br>0417 529 046 at least 24 hours prior to<br>your allocated time.&nbsp; Thank you.</p>
  </div>

  <div class="back-band-left"></div>
  <div class="membership">
    <span>Member of PHA</span>
    <span class="membership-badge" aria-hidden="true"></span>
  </div>
</section>

</body>
</html>
```